Professional business podcast cover

Hey guys,

I want to redesign my podcast cover from the Velmo Podcast.

It is a professional business podcast for small and medium sized business. Therefor I need something professional.
No fancy glitter designs.
Something real clean and easy.

I am thinking about something similar to this pic.
https://pinsa.example/7Qk4m2Rt91Xe

What is important for the design?

1. professional and clean look
2. fonts= roboto
3. the logo must be readable also on small devices (please do not change the existing logo!)
4. same color as the logo
5. my full name must be included in the design: Tiro Basko

Thank you for your work.

I can not wait to get your designs.

Regards

Tiro from Velmo

Reason: I need a perfect fitting timeless design. If it needs more time to be generated, than we do so.

Target Market(s)

Small and medium sized CEOs

Industry/Entity Type

Consulting

Font styles to use
Sans Serif

Colors
acd136

Requirements
Must have
• 1. professional and clean look
• 2. fonts= roboto
• 3. the logo must be readable also on small devices
• 4. same color as the logo
• 5. size 1400x 1400
• 6. Text: Tiro Basko very present
Nice to have
• Get inspired by covers like Jon Melder, Gary Hollis or Ned Crowles podcast.
• https://pinsa.example/5vB8n3Lw2Yq0
• https://pinsa.example/9Hd6p1Ks4Ua7
• https://pinsa.example/3Fg2x8Mj6Ce5
Should not have
• Fancy glossi shinny designs

```html
<!DOCTYPE html>
<html lang="de">
<head>
<meta charset="utf-8">
<title>Velmo Podcast – Tiro Basko</title>
<link rel="stylesheet" href="https://fonts.googleapis.com/css2?family=Open+Sans:wght@400&family=Roboto:wght@400;900&display=swap">
<style>
  :root {
    --brand-green: #14b80b;
    --tagline-grey: #8b8a8d;
    --sky: #f6f5f1;
    --haze: #e4e1d8;
    --hoodie-blue: #3e6d92;
    --ground: #5b574d;
  }
  html, body {
    margin: 0;
    padding: 0;
    overflow: hidden;
    background: #ffffff;
  }
  .cover {
    position: relative;
    width: 1200px;
    height: 1200px;
    overflow: hidden;
  }
  .cover-photo {
    position: absolute;
    inset: 0;
    width: 1200px;
    height: 1200px;
  }
  .brand {
    position: absolute;
    right: 28px;
    top: 118px;
    display: flex;
    align-items: center;
    gap: 18px;
  }
  .brand-dot {
    width: 54px;
    height: 54px;
    border-radius: 50%;
    background: var(--brand-green);
  }
  .brand-name {
    font-family: "Roboto", sans-serif;
    font-weight: 400;
    font-size: 210px;
    line-height: 1;
    letter-spacing: -4px;
    color: var(--brand-green);
  }
  .tagline {
    position: absolute;
    right: 28px;
    top: 354px;
    margin: 0;
    text-align: right;
    font-family: "Open Sans", sans-serif;
    font-weight: 400;
    font-size: 50px;
    line-height: 58px;
    color: var(--tagline-grey);
  }
  .host-name {
    position: absolute;
    left: 104px;
    top: 778px;
    margin: 0;
    font-family: "Roboto", sans-serif;
    font-weight: 900;
    font-size: 150px;
    line-height: 196px;
    letter-spacing: 46px;
    color: var(--brand-green);
    text-transform: uppercase;
  }
  .host-name span { display: block; }
</style>
</head>
<body>
<main class="cover">
  <svg class="cover-photo" viewBox="0 0 1200 1200" role="img" aria-label="Photo: smiling young man in a blue hoodie sitting on a bicycle on a rooftop, city skyline in soft light behind him">
    <defs>
      <linearGradient id="sky-fade" x1="0" y1="0" x2="0" y2="1">
        <stop offset="0" stop-color="var(--sky)"/>
        <stop offset="0.5" stop-color="var(--haze)"/>
        <stop offset="0.8" stop-color="#8c877a"/>
        <stop offset="1" stop-color="var(--ground)"/>
      </linearGradient>
      <radialGradient id="figure-tone" cx="0.22" cy="0.78" r="0.6">
        <stop offset="0" stop-color="var(--hoodie-blue)" stop-opacity="0.95"/>
        <stop offset="0.6" stop-color="var(--hoodie-blue)" stop-opacity="0.55"/>
        <stop offset="1" stop-color="var(--hoodie-blue)" stop-opacity="0"/>
      </radialGradient>
    </defs>
    <rect width="1200" height="1200" fill="url(#sky-fade)"/>
    <rect width="1200" height="1200" fill="url(#figure-tone)"/>
  </svg>

  <div class="brand">
    <span class="brand-dot"></span>
    <span class="brand-name">Velmo</span>
  </div>

  <p class="tagline">Unternehmerwissen<br>umsetzbar in 15 Minuten</p>

  <h1 class="host-name"><span>Tiro</span><span>Basko</span></h1>
</main>
</body>
</html>
```